Brindle Works Australia Website

Brindle Works Australia (BWA) is a Industrial, Mining & Transport Services provider in Australia. We require a website that is both pc and mobile freindly. The website will be used to both present our company services and give us exposure in a crowded market. The main page of the website will have a snapshot of who BWA is and its from this page that the user can click to enter the area of interest ie. Industrial, Mining and Transport. A disticted logo can be used to indicate the area in question.<br/>Within the industrial, Mining and the Transport services pages will need list and description of services that are provided, current customer lists and news pages.<br/>The website will need a contacts page so prospective customers can get in contact with BWA.<br/>The website design will require a user freindly back end so future updates and ammendments can be carriedout by less experienced people within the BWA business.

Target Market(s)

Industrial, Mining and Transport Services provider markets

Coding

Coded - Design and coding required

Number of Pages Required

5+ page

Font styles to use
Sans Serif

Colors
00a990

Requirements
Must have
• Ability to build servises with in services. because the main service area is only the main service with in each service group there is alot of smaller services / tasks.
• Key wording for easy seach engine capabilities. The website will need to be search engine freindly.

```html
<!DOCTYPE html>
<html lang="en">
<head>
<meta charset="utf-8">
<title>Brindle Works Australia – Industrial, Mining & Transport Services</title>
<link href="https://fonts.googleapis.com/css2?family=Poppins:wght@400;500;600&family=Oswald:wght@500&display=swap" rel="stylesheet">
<style>
:root{
  --green:#1f8c19;
  --green-dark:#17780f;
  --ink:#1b1b1b;
  --text:#666;
  --light:#efefef;
  --footer:#1f1f1f;
  --white:#fff;
}
*{margin:0;padding:0;box-sizing:border-box}
html,body{width:1200px;height:3703px;overflow:hidden}
body{position:relative;font-family:'Poppins',sans-serif;color:var(--text);background:var(--white)}
.abs{position:absolute}
a{color:inherit;text-decoration:none}

/* header */
.site-header{left:0;top:0;width:1200px;height:84px;background:var(--white)}
.brand{left:77px;top:18px;display:flex;align-items:center;gap:10px}
.brand-mark{width:40px;height:40px;background:var(--green)}
.brand-name{font-weight:600;font-size:14px;line-height:16px;color:var(--green);text-transform:uppercase}
.main-nav a{position:absolute;top:33px;font-size:14px;color:#333;text-transform:uppercase}
.main-nav a.active{color:var(--green)}
.nav-bar{left:590px;top:0;width:64px;height:4px;background:var(--green)}

/* hero */
.hero{left:0;top:84px;width:1200px;height:593px;background:linear-gradient(180deg,#cdd3d6 0%,#a9adaa 45%,#7c7a72 100%)}
.hero-ring{left:707px;top:160px;width:412px;height:412px;border-radius:50%;background:rgba(70,70,70,.6)}
.hero-disc{left:729px;top:182px;width:368px;height:368px;border-radius:50%;background:var(--green)}
.hero-title{left:739px;top:278px;width:348px;text-align:center;font-family:'Oswald',sans-serif;font-weight:500;font-size:35px;line-height:50px;letter-spacing:-.3px;white-space:nowrap;color:var(--white);text-transform:uppercase}
.hero-btn{left:829px;top:452px;width:177px;height:50px;border:1.5px solid var(--white);border-radius:25px;color:var(--white);font-weight:500;font-size:18px;text-align:center;line-height:47px}

/* welcome */
.welcome{left:0;top:677px;width:1200px;height:427px;background:var(--green);color:var(--white);text-align:center}
.welcome h1{position:absolute;left:0;top:55px;width:1200px;font-size:43px;font-weight:600;letter-spacing:.5px}
.welcome .sub{position:absolute;left:0;top:116px;width:1200px;font-size:16px}
.welcome .copy{position:absolute;left:345px;top:166px;width:510px;font-size:14.5px;line-height:27px}
.welcome .copy p+p{margin-top:14px}
.down{left:564px;top:1066px;width:72px;height:72px;border-radius:50%;background:var(--white)}
.down-inner{left:574px;top:1076px;width:52px;height:52px;border-radius:50%;background:var(--green)}

/* services */
.service-band{left:0;width:1200px}
.band-mining{top:1598px;height:469px;background:linear-gradient(120deg,#e6e6e6 0%,#f6f6f6 45%,#dcdcdc 100%)}
.photo{border-radius:50%}
.icon-ring{width:110px;height:110px;border-radius:50%;background:var(--white)}
.icon-disc{width:90px;height:90px;border-radius:50%;background:var(--green)}
.service h2{position:absolute;font-size:38px;font-weight:600;color:var(--ink);text-transform:uppercase}
.service p{position:absolute;width:400px;font-size:14.5px;line-height:27px}
.btn{position:absolute;width:177px;height:50px;border-radius:25px;background:var(--green);color:var(--white);font-weight:500;font-size:18px;text-align:center;line-height:50px}

/* news */
.news{left:0;top:2535px;width:1200px;height:645px;background:var(--light)}
.news h2{position:absolute;left:0;top:55px;width:1200px;text-align:center;font-size:40px;font-weight:600;color:var(--ink)}
.card{top:2670px;width:302px;height:448px;background:var(--white)}
.card-img{position:absolute;left:0;top:0;width:302px;height:208px}
.card h3{position:absolute;left:23px;top:238px;font-size:15.5px;font-weight:600;color:var(--ink);text-transform:uppercase}
.card .date{position:absolute;left:25px;top:268px;font-size:14px;color:var(--green)}
.card p{position:absolute;left:23px;top:310px;width:240px;font-size:14px;line-height:26px}
.card .more{position:absolute;left:23px;top:405px;font-size:14px;font-weight:500;color:var(--green);text-decoration:underline}

/* clients */
.clients{left:0;top:3180px;width:1200px;height:131px;background:var(--white)}
.client{position:absolute;top:44px;display:flex;align-items:center;gap:8px;font-size:28px;line-height:40px;font-weight:600;color:#555}
.client i{display:block;width:22px;height:22px;background:#9a9a9a}

/* newsletter */
.newsletter{left:0;top:3311px;width:1200px;height:104px;background:var(--green)}
.newsletter h3{position:absolute;left:167px;top:33px;font-size:28px;font-weight:500;color:var(--white)}
.field{left:543px;top:3338px;width:479px;height:50px;border-radius:25px;background:rgba(255,255,255,.3);border:2px solid rgba(255,255,255,.55)}
.field span{position:absolute;left:22px;top:14px;font-size:14px;color:var(--white)}
.subscribe{left:866px;top:3342px;width:150px;height:42px;border-radius:21px;background:var(--green-dark);color:var(--white);font-weight:600;font-size:16px;text-align:center;line-height:42px}

/* footer */
.site-footer{left:0;top:3415px;width:1200px;height:288px;background:var(--footer);color:#bdbdbd}
.foot-brand{left:78px;top:3478px;display:flex;align-items:center;gap:12px}
.foot-brand .brand-mark{width:52px;height:52px}
.foot-brand .brand-name{font-size:18px;line-height:21px}
.social{top:3565px;width:46px;height:46px;border-radius:50%}
.copyright{left:79px;top:3628px;font-size:14px;color:var(--white)}
.foot-h{font-size:18px;font-weight:500;color:var(--white)}
.sitemap li{position:absolute;left:681px;list-style:none;font-size:14px;color:#bdbdbd;display:flex;align-items:center;gap:10px}
.sitemap li::before{content:"";width:5px;height:5px;border-radius:50%;background:var(--green)}
.contact-line{left:923px;font-size:14px;line-height:25px;color:#bdbdbd}
</style>
</head>
<body>

<header class="site-header abs">
  <div class="brand abs">
    <span class="brand-mark"></span>
    <span class="brand-name">Brindle Works<br>Australia</span>
  </div>
  <span class="nav-bar abs"></span>
  <nav class="main-nav">
    <a class="active" style="left:602px">Home</a>
    <a style="left:681px">About</a>
    <a style="left:759px">Services</a>
    <a style="left:853px">Clients</a>
    <a style="left:939px">News</a>
    <a style="left:1006px">Contact</a>
  </nav>
  <svg class="abs" style="left:1107px;top:34px" width="16" height="16" viewBox="0 0 16 16"><circle cx="6.5" cy="6.5" r="5" fill="none" stroke="#222" stroke-width="2"/><line x1="10" y1="10" x2="15" y2="15" stroke="#222" stroke-width="2.2"/></svg>
</header>

<section class="hero abs" role="img" aria-label="Large yellow haul truck on a quarry road under a cloudy sky"></section>
<svg class="abs" style="left:32px;top:334px" width="20" height="38" viewBox="0 0 20 38"><polyline points="18,2 2,19 18,36" fill="none" stroke="#222" stroke-width="2"/></svg>
<svg class="abs" style="left:1155px;top:334px" width="20" height="38" viewBox="0 0 20 38"><polyline points="2,2 18,19 2,36" fill="none" stroke="#222" stroke-width="2"/></svg>
<div class="hero-ring abs"></div>
<div class="hero-disc abs"></div>
<h2 class="hero-title abs">BWA Industrial,<br>Mining &amp; Transport<br>Services</h2>
<a class="hero-btn abs">CONTACT US</a>

<section class="welcome abs">
  <h1>WELCOME TO BWA</h1>
  <div class="sub">BRINDLE WORKS AUSTRALIA</div>
  <div class="copy">
    <p>Lorem Ipsum is simply dummy text of the printing and typesetting industry. Lorem Ipsum has been the industry's standard.</p>
    <p>Lorem Ipsum is simply dummy text of the printing and typesetting industry. Lorem Ipsum has been the industry's standard dummy text ever since the 1500s, when an unknown printer took a galley of type scrambled it to make a typebook.</p>
  </div>
</section>
<div class="down abs"></div>
<div class="down-inner abs"></div>
<svg class="abs" style="left:590px;top:1094px" width="20" height="14" viewBox="0 0 20 14"><polyline points="3,3 10,9 17,3" fill="none" stroke="#fff" stroke-width="1.6"/><polyline points="3,7 10,13 17,7" fill="none" stroke="#fff" stroke-width="1.6"/></svg>

<!-- Industrial -->
<section class="service">
  <div class="photo abs" style="left:144px;top:1198px;width:334px;height:334px;background:linear-gradient(180deg,#a99ac8 0%,#e7b7a5 50%,#3a3a4a 100%)" role="img" aria-label="Refinery plant lit up at dusk"></div>
  <div class="icon-ring abs" style="left:372px;top:1417px"></div>
  <div class="icon-disc abs" style="left:382px;top:1427px"></div>
  <svg class="abs" style="left:405px;top:1450px" width="44" height="44" viewBox="0 0 44 44" fill="#fff"><path d="M4 40V24l9-6v6l9-6v6l9-6V10h6v30z"/><rect x="9" y="30" width="4" height="4" fill="#1f8c19"/><rect x="18" y="30" width="4" height="4" fill="#1f8c19"/><rect x="27" y="30" width="4" height="4" fill="#1f8c19"/></svg>
  <h2 style="left:621px;top:1240px">Industrial</h2>
  <p style="left:624px;top:1298px">BWA Industrial Services Division offers an integrated site service and maintenance of your fixed plant. Our team are experienced in developing site-specific maintenance / service plans to ensure you critical site equipment stays operational.</p>
  <a class="btn" style="left:625px;top:1450px">LEARN MORE</a>
</section>

<!-- Mining -->
<section class="service">
  <div class="service-band band-mining abs"></div>
  <h2 style="left:147px;top:1714px">Mining</h2>
  <p style="left:149px;top:1772px">BWA Mining Services Division offers an integrated service in equipment rental, maintenance and earthmoving. Supported by a modern and comprehensive fleet and experienced mechanical technicians that have previous.</p>
  <a class="btn" style="left:152px;top:1924px">LEARN MORE</a>
  <div class="photo abs" style="left:743px;top:1662px;width:334px;height:334px;background:linear-gradient(180deg,#7f8ea0 0%,#8a8478 50%,#4a4640 100%)" role="img" aria-label="Haul truck loaded by an excavator at a mine face"></div>
  <div class="icon-ring abs" style="left:740px;top:1881px"></div>
  <div class="icon-disc abs" style="left:750px;top:1891px"></div>
  <svg class="abs" style="left:773px;top:1914px" width="44" height="44" viewBox="0 0 44 44" fill="#fff"><rect x="10" y="12" width="14" height="12"/><rect x="6" y="22" width="26" height="8"/><rect x="4" y="31" width="30" height="7" rx="3.5"/><path d="M32 20l8 2v12l-6-3z"/></svg>
</section>

<!-- Transport -->
<section class="service">
  <div class="photo abs" style="left:144px;top:2128px;width:334px;height:334px;background:linear-gradient(180deg,#9fb5d6 0%,#d6d2c4 50%,#5c5c5c 100%)" role="img" aria-label="Semi-trailer trucks on an open highway"></div>
  <div class="icon-ring abs" style="left:372px;top:2346px"></div>
  <div class="icon-disc abs" style="left:382px;top:2356px"></div>
  <svg class="abs" style="left:405px;top:2379px" width="44" height="44" viewBox="0 0 44 44" fill="#fff"><rect x="4" y="10" width="22" height="20"/><path d="M27 16h8l5 8v8H27z"/><circle cx="11" cy="34" r="4"/><circle cx="33" cy="34" r="4"/></svg>
  <h2 style="left:621px;top:2169px">Transport</h2>
  <p style="left:624px;top:2227px">BWA Transport Division specialises in the transport - ation of all types of materials such as, Steel, Structural Steel, Concrete Building Panels, Machinery, Palletised freight and bulk products.r, all of which are handled with the same amount of care.</p>
  <a class="btn" style="left:625px;top:2380px">LEARN MORE</a>
</section>

<!-- News -->
<section class="news abs"><h2>LATEST NEWS</h2></section>
<article class="card abs" style="left:126px">
  <div class="card-img" style="background:linear-gradient(180deg,#8aa4c4 0%,#c8b48c 60%,#8c7650 100%)" role="img" aria-label="Worker looking at a bucket-wheel excavator in an open field"></div>
  <h3>Lorem Ipsum is text print</h3><div class="date">08 jan 2020</div>
  <p>Lorem Ipsum is simply dummy text of the printing &amp; typesetting simpe industry Ipsum text.</p>
  <a class="more">Read More »</a>
</article>
<article class="card abs" style="left:450px">
  <div class="card-img" style="background:linear-gradient(180deg,#6d7fb8 0%,#d59a8e 40%,#5c6a5a 100%)" role="img" aria-label="Trucks on a multi-lane highway at sunset"></div>
  <h3>Lorem Ipsum is text print</h3><div class="date">08 jan 2020</div>
  <p>Lorem Ipsum is simply dummy text of the printing &amp; typesetting simpe industry Ipsum text.</p>
  <a class="more">Read More »</a>
</article>
<article class="card abs" style="left:772px">
  <div class="card-img" style="background:linear-gradient(180deg,#2f3336 0%,#5d5a54 60%,#3a3733 100%)" role="img" aria-label="Underground mine tunnel with drilling rig"></div>
  <h3>Lorem Ipsum is text print</h3><div class="date">08 jan 2020</div>
  <p>Lorem Ipsum is simply dummy text of the printing &amp; typesetting simpe industry Ipsum text.</p>
  <a class="more">Read More »</a>
</article>

<!-- Clients -->
<section class="clients abs" aria-label="Clients">
  <span class="client" style="left:80px"><i></i>Garrow</span>
  <span class="client" style="left:262px">Sitvale</span>
  <span class="client" style="left:420px"><i></i>Tarco</span>
  <span class="client" style="left:580px"><i></i>Ulmen</span>
  <span class="client" style="left:760px">Meridan</span>
  <span class="client" style="left:945px"><i></i>Alston</span>
</section>

<!-- Newsletter -->
<section class="newsletter abs"><h3>Sign Up For Newsletter !</h3></section>
<div class="field abs"><span>Enter Email *</span></div>
<a class="subscribe abs">SUBSCRIBE</a>

<!-- Footer -->
<footer class="site-footer abs"></footer>
<div class="foot-brand abs">
  <span class="brand-mark"></span>
  <span class="brand-name">Brindle Works<br>Australia</span>
</div>
<span class="social abs" style="left:79px;background:#3b5998" aria-label="Social link"></span>
<span class="social abs" style="left:131px;background:#1da1f2" aria-label="Social link"></span>
<span class="social abs" style="left:183px;background:#d9261c" aria-label="Social link"></span>
<span class="social abs" style="left:236px;background:#dd4b39" aria-label="Social link"></span>
<div class="copyright abs">©BWA - 2020 All rights reserved.</div>

<div class="foot-h abs" style="left:681px;top:3449px">SITEMAP</div>
<ul class="sitemap">
  <li style="top:3499px">Home</li>
  <li style="top:3528px">About</li>
  <li style="top:3557px">Services</li>
  <li style="top:3586px">Clients</li>
  <li style="top:3615px">News</li>
  <li style="top:3644px">Contact</li>
</ul>

<div class="foot-h abs" style="left:890px;top:3449px">CONTACT US</div>
<svg class="abs" style="left:890px;top:3502px" width="18" height="26" viewBox="0 0 18 26"><path d="M9 1a8 8 0 0 0-8 8c0 6 8 16 8 16s8-10 8-16a8 8 0 0 0-8-8z" fill="#1f8c19"/><circle cx="9" cy="9" r="3" fill="#1f1f1f"/></svg>
<div class="contact-line abs" style="top:3497px">BWA<br>101 - Lorem ipsum simple<br>text print type industry</div>
<svg class="abs" style="left:889px;top:3598px" width="18" height="18" viewBox="0 0 18 18"><path d="M4 1l3 4-2 2c1 3 3 5 6 6l2-2 4 3-2 3C8 17 1 10 1 3z" fill="#1f8c19"/></svg>
<div class="contact-line abs" style="top:3595px">123 555 0190</div>
<svg class="abs" style="left:889px;top:3642px" width="20" height="14" viewBox="0 0 20 14"><rect width="20" height="14" fill="#1f8c19"/><polyline points="1,1 10,8 19,1" fill="none" stroke="#1f1f1f" stroke-width="1.6"/></svg>
<div class="contact-line abs" style="top:3637px">info@BWA.com</div>

</body>
</html>
```